Header für Blog zur Organisationsentwicklung
LunaKrie hat die Hinweise im Briefing und in den Kommentaren zu vorhandenen Designs gut aufgenommen und den Gestaltungsprozess vorangetrieben. So bekomme ich ein tolles Design, wo ich vorher keine Ahnung hatte, wie es aussehen sollte.
Zielgruppe
Ich bin freiberuflicher Organisationsberater und pflege auf meiner Website ein Blog zur Organisationsentwicklung. Dieses Blog soll zukünftig auf einer eigenen Domain erscheinen, sodass auch andere Kollegen sich daran beteiligen können. Daher soll mein Name nicht mehr im Vordergrund stehen - wenngleich ich immer noch als der Macher des Blog erkennbar bleiben soll.
Aufgabenstellung
Für das Blog "Labor für Unternehmenswandel" www.uw-labor.de wird ein ansprechender Header gesucht.
Der Header sollte den Namen des Blog und ein grafisches Element enthalten, dass der Bildsprache "Werkstatt", "Organisation", "Führung", etc. entnommen ist. Eventuell ein Element, das die Bildsprachen verbindet?
Da das Blog von einem Foto-Slider unter dem Header geprägt ist, sollte der Header nicht einfach aus einem Foto bestehen.
Die Farbgebung des Blog stellt die grafische Verbindung zu meiner Website www.hasselkamp.com her.
Mein Logo sollte im Header nicht verwendet werden, da ich das Blog bewusst von meiner Website löse, um weitere Beraterkollegen einzuladen, dabei mitzumachen

```html
<!DOCTYPE html>
<html lang="de">
<head>
<meta charset="UTF-8">
<title>Labor für Unternehmenswandel – Blog-Header</title>
<link href="https://fonts.googleapis.com/css2?family=Source+Sans+3:wght@600&display=swap" rel="stylesheet">
<style>
  :root {
    --header-bg: #31306a;
    --header-ink: #ffffff;
  }
  html, body {
    margin: 0;
    padding: 0;
    width: 1200px;
    height: 102px;
    overflow: hidden;
    background: var(--header-bg);
  }
  .blog-header {
    position: relative;
    width: 1200px;
    height: 102px;
    background: var(--header-bg);
    display: flex;
    align-items: center;
    justify-content: space-between;
    box-sizing: border-box;
    padding: 0 58px 0 39px;
  }
  .blog-title {
    margin: 0;
    font-family: "Source Sans 3", "Source Sans Pro", sans-serif;
    font-weight: 600;
    font-size: 35px;
    letter-spacing: 0.1px;
    color: var(--header-ink);
    line-height: 1;
    padding-bottom: 4px;
  }
  .theme-icons {
    display: flex;
    align-items: center;
    gap: 30px;
  }
  .theme-icon {
    width: 54px;
    height: 54px;
    display: block;
  }
</style>
</head>
<body>
  <header class="blog-header">
    <h1 class="blog-title">Labor für Unternehmenswandel</h1>
    <div class="theme-icons">
      <!-- Werkzeug -->
      <svg class="theme-icon icon-wrench" viewBox="0 0 48 48" role="img" aria-label="Schraubenschlüssel">
        <line x1="8" y1="40" x2="28" y2="20" stroke="var(--header-ink)" stroke-width="7" stroke-linecap="round"/>
        <circle cx="32" cy="16" r="11" fill="var(--header-ink)"/>
        <rect x="34" y="2" width="8" height="18" fill="var(--header-bg)" transform="rotate(45 38 11)"/>
        <circle cx="9" cy="39" r="1.8" fill="var(--header-bg)"/>
      </svg>
      <!-- Organigramm -->
      <svg class="theme-icon icon-hierarchy" viewBox="0 0 48 48" role="img" aria-label="Organigramm">
        <rect x="17" y="4" width="14" height="11" rx="1.5" fill="var(--header-ink)"/>
        <path d="M24 15 V24 M8 31 V24 H40 V31 M24 24 V31" stroke="var(--header-ink)" stroke-width="3" fill="none"/>
        <rect x="2" y="31" width="12" height="11" rx="1.5" fill="var(--header-ink)"/>
        <rect x="18" y="31" width="12" height="11" rx="1.5" fill="var(--header-ink)"/>
        <rect x="34" y="31" width="12" height="11" rx="1.5" fill="var(--header-ink)"/>
      </svg>
      <!-- Team -->
      <svg class="theme-icon icon-team" viewBox="0 0 48 48" role="img" aria-label="Personengruppe">
        <circle cx="9" cy="13" r="5.5" fill="var(--header-ink)"/>
        <circle cx="39" cy="13" r="5.5" fill="var(--header-ink)"/>
        <path d="M0 32 V25 Q0 20 6 20 H13 Q9 24 9 29 V32 Z" fill="var(--header-ink)"/>
        <path d="M48 32 V25 Q48 20 42 20 H35 Q39 24 39 29 V32 Z" fill="var(--header-ink)"/>
        <circle cx="24" cy="14" r="8" fill="var(--header-ink)"/>
        <path d="M11 42 V31 Q11 24 18 24 H30 Q37 24 37 31 V42 Z" fill="var(--header-ink)"/>
      </svg>
    </div>
  </header>
</body>
</html>
```